Meadow Hollow Beauty brand redesign of product labels

national rebrand of skincare product labels - same design but 6 sizes. Will be used for facial serums, body oils, bath salts, room sprays, etc. All labels to be same design - just adjusted for the different sizes. See brand document and sample label.

Bottle Specifications are located in the branding file.
Fonts included in product branding document.
Colours included in branding document.

Featuring company name and logo, product name, product feature, ingredients, size, directions, tag line. See attached sample label as example for design.

Black label base - matt.

Target Market(s)

Natural beauty, 20-60

Industry/Entity Type

farming, natural beauty

Font styles to use
Sans Serif

Requirements
Must have
• Modern, clean, homey
Nice to have
• modern clean design - using the branding colours provided
Should not have
• busy, crowded,

```html
<!DOCTYPE html>
<html lang="en">
<head>
<meta charset="UTF-8">
<title>Meadow Hollow Beauty – Product Labels</title>
<link rel="stylesheet" href="https://fonts.googleapis.com/css2?family=Raleway:wght@400;500&display=swap">
<style>
  :root {
    --backdrop: #d6d6d6;
    --label-black: #141414;
    --sage: #b7cf92;
    --sage-soft: #c9dba9;
    --teal: #6a9b97;
    --teal-deep: #4f7f7c;
    --muted-text: #8a8a8a;
    --band-text: #1d2a17;
  }
  * { box-sizing: border-box; margin: 0; padding: 0; }
  html, body {
    width: 1200px; height: 1200px; overflow: hidden;
    background: var(--backdrop);
    font-family: "Raleway", sans-serif;
  }
  .canvas {
    position: relative; width: 1200px; height: 1200px;
    background: radial-gradient(circle at 50% 40%, #e4e4e4 0%, var(--backdrop) 70%);
  }
  .label {
    position: absolute;
    background: var(--label-black);
    border-radius: 6px;
    color: var(--sage);
    text-align: center;
    overflow: hidden;
  }
  .brand-name {
    position: absolute; left: 0; right: 0;
    color: var(--sage);
    font-weight: 400;
    letter-spacing: 0;
    line-height: 1.2;
  }
  .sprig {
    position: absolute;
    border-radius: 40px;
    background: linear-gradient(160deg, var(--sage-soft) 0%, var(--teal) 60%, var(--teal-deep) 100%);
    opacity: 0.55;
  }
  .product-name {
    position: absolute; left: 0; right: 0;
    font-weight: 400; color: var(--sage);
    letter-spacing: 0.02em; line-height: 1.1;
  }
  .variant-band {
    position: absolute; left: 50%; transform: translateX(-50%);
    background: var(--sage);
    color: var(--band-text);
    font-weight: 500;
    white-space: nowrap;
  }
  .size {
    position: absolute; left: 0; right: 0;
    color: var(--muted-text);
  }

  /* Body oil label */
  .label--body-oil { left: 180px; top: 300px; width: 400px; height: 620px; }
  .label--body-oil .brand-name { top: 150px; font-size: 32px; }
  .label--body-oil .sprig { right: 18px; top: 330px; width: 46px; height: 270px; }
  .label--body-oil .product-name { top: 395px; font-size: 50px; }
  .label--body-oil .variant-band { top: 470px; font-size: 20px; padding: 8px 22px; }
  .label--body-oil .size { top: 545px; font-size: 15px; }

  /* Facial serum label */
  .label--serum { left: 750px; top: 150px; width: 180px; height: 300px; }
  .label--serum .brand-name { top: 60px; font-size: 15px; }
  .label--serum .sprig { right: 8px; top: 120px; width: 20px; height: 160px; }
  .label--serum .product-name { top: 160px; font-size: 22px; }
  .label--serum .variant-band { top: 220px; font-size: 8px; padding: 3px 7px; }
  .label--serum .size { top: 250px; font-size: 8px; }

  /* Bath salts label */
  .label--bath-salts { left: 640px; top: 560px; width: 420px; height: 300px; }
  .label--bath-salts .brand-name { top: 55px; font-size: 19px; }
  .label--bath-salts .sprig { right: 30px; top: 60px; width: 34px; height: 220px; }
  .label--bath-salts .product-name { top: 170px; font-size: 26px; }
  .label--bath-salts .variant-band { top: 210px; font-size: 11px; padding: 5px 22px; }
  .label--bath-salts .size { top: 250px; font-size: 9px; }
</style>
</head>
<body>
<main class="canvas">

  <section class="label label--body-oil" aria-label="Body oil label">
    <p class="brand-name">Meadow Hollow<br>Beauty</p>
    <div class="sprig" role="img" aria-label="Green and teal leafy sprig decoration"></div>
    <h2 class="product-name">BODY OIL</h2>
    <p class="variant-band">COCONUT &amp; JASMIN</p>
    <p class="size">40 oz</p>
  </section>

  <section class="label label--serum" aria-label="Facial serum label">
    <p class="brand-name">Meadow Hollow<br>Beauty</p>
    <div class="sprig" role="img" aria-label="Green and teal leafy sprig decoration"></div>
    <h2 class="product-name">FACIAL<br>SERUM</h2>
    <p class="variant-band">COCONUT &amp; JASMIN</p>
    <p class="size">40 oz</p>
  </section>

  <section class="label label--bath-salts" aria-label="Bath salts label">
    <p class="brand-name">Meadow Hollow<br>Beauty</p>
    <div class="sprig" role="img" aria-label="Green and teal leafy sprig decoration"></div>
    <h2 class="product-name">BATH SALTS</h2>
    <p class="variant-band">NO ADDED SCENTS</p>
    <p class="size">40 oz</p>
  </section>

</main>
</body>
</html>
```